I need the Scorecard I've developed for my staff to be produced into a visually engaging piece that will encourage the staff to utilize it on a daily basis. I'm thinking it could be 5x7 in size so that it isn't too cumbersome, but I'm open to different layouts.
I have multiple other departments that will need Scorecards created for them as well, but each one will contain task specific questions for each department.

```html
<!DOCTYPE html>
<html lang="en">
<head>
<meta charset="utf-8">
<title>Receptionist Daily Excellence Scorecard</title>
<link rel="stylesheet" href="https://fonts.googleapis.com/css2?family=Catamaran:wght@500;600;700&family=Gelasio:wght@400&family=Arimo:wght@400&display=swap">
<style>
:root{
  --indigo:#3f3a8e;
  --magenta:#9c3d92;
  --ink:#222;
  --rule:#a9a9a9;
  --panel:#f4f4f4;
  --white:#fff;
  --star:#f2b51c;
  --page:#e9e7ee;
}
*{box-sizing:border-box;margin:0;padding:0}
html,body{width:918px;height:1200px;overflow:hidden;background:var(--page)}
.stage{position:relative;width:918px;height:1200px}
.scorecard{position:absolute;left:30px;top:0;width:750px;height:1049px;transform:scale(1.144);transform-origin:0 0;background:var(--white);overflow:hidden;font-family:"Arimo",Arial,sans-serif;color:var(--ink)}
.abs{position:absolute}
.serif{font-family:"Gelasio",Georgia,serif}
.heading{font-family:"Catamaran",sans-serif;font-weight:600;white-space:nowrap}
.rule{position:absolute;height:0;border-bottom:1px solid var(--rule)}
.band{position:absolute;left:0;width:750px}
.band--grey{background:var(--panel)}
.band--footer{background:var(--indigo);color:var(--white)}
.title-line1{left:16px;top:28px;font-size:34px;color:var(--indigo);font-weight:600}
.title-line2{left:16px;top:70px;font-size:34px;color:var(--magenta);font-weight:600}
.field-label{font-size:18px;color:var(--ink)}
.section-title{font-size:22px;color:var(--magenta)}
.section-title small{font-size:16px;font-weight:600}
.section-title--indigo{color:var(--indigo)}
.scale-key{font-size:16px;top:306px}
.col-head{font-size:16px;color:var(--indigo);top:396px}
.task{font-size:14.5px;left:64px}
.option{font-size:15px;color:var(--indigo)}
.option-desc{font-size:12.5px;line-height:17px;color:var(--ink)}
.radio{width:14px;height:14px;border:1.5px solid var(--ink);border-radius:50%}
.question{font-size:13px;color:var(--indigo)}
.question b{color:var(--magenta);font-size:15px;margin-right:6px}
.sub{font-size:13px;color:var(--indigo)}
.sub span{font-size:10px}
.footer-label{font-family:"Gelasio",Georgia,serif;font-size:16px}
</style>
</head>
<body>
<div class="stage">
<main class="scorecard">

  <!-- header -->
  <svg class="abs" style="left:0;top:0" width="750" height="260" viewBox="0 0 750 260" aria-hidden="true">
    <rect width="750" height="260" fill="#f7f7f7"/>
    <path d="M0,0 H750 V226 C700,110 520,10 0,0 Z" fill="var(--indigo)"/>
    <path d="M0,4 C520,20 705,122 750,250 V236 C702,118 520,14 0,2 Z" fill="var(--magenta)"/>
    <g fill="none" stroke="#fff" stroke-width="2.5" stroke-linejoin="round">
      <path d="M662,14 H700 L710,24 V80 H662 Z"/>
      <path d="M700,14 V24 H710"/>
      <rect x="669" y="30" width="7" height="7"/><line x1="681" y1="33" x2="703" y2="33"/>
      <rect x="669" y="44" width="7" height="7"/><line x1="681" y1="47" x2="703" y2="47"/>
      <rect x="669" y="58" width="7" height="7"/><line x1="681" y1="61" x2="703" y2="61"/>
      <path d="M650,108 V84 C650,76 656,72 662,76 L668,80 V70 C668,66 674,66 674,70 V92 C674,100 668,106 660,108"/>
    </g>
  </svg>
  <div class="abs heading title-line1">Receptionist</div>
  <div class="abs heading title-line2">Daily Excellence Scorecard</div>
  <div class="abs serif field-label" style="left:16px;top:134px">Name:</div>
  <div class="rule" style="left:78px;top:151px;width:166px"></div>
  <div class="abs serif field-label" style="left:16px;top:185px">Date:</div>
  <div class="rule" style="left:78px;top:203px;width:166px"></div>
  <div class="abs serif field-label" style="left:270px;top:185px">Location:</div>
  <div class="rule" style="left:356px;top:203px;width:156px"></div>

  <!-- rating key -->
  <section class="band" style="top:248px;height:99px;background:var(--white)">
    <div class="abs heading section-title" style="left:16px;top:12px">Please Rate Yourself For Each Task</div>
    <svg class="abs" style="left:605px;top:12px" width="86" height="26" viewBox="0 0 86 26" aria-hidden="true">
      <g fill="none" stroke="var(--magenta)" stroke-width="1.3">
        <path d="M8,12 l2,4 4,.5 -3,3 1,4 -4,-2 -4,2 1,-4 -3,-3 4,-.5z"/>
        <path d="M24,8 l2.3,4.6 5,.7 -3.6,3.5 .9,5 -4.6,-2.4 -4.6,2.4 .9,-5 -3.6,-3.5 5,-.7z"/>
        <path d="M43,2 l2.8,5.6 6,.9 -4.4,4.3 1,6 -5.4,-2.8 -5.4,2.8 1,-6 -4.4,-4.3 6,-.9z"/>
        <path d="M62,8 l2.3,4.6 5,.7 -3.6,3.5 .9,5 -4.6,-2.4 -4.6,2.4 .9,-5 -3.6,-3.5 5,-.7z"/>
        <path d="M78,12 l2,4 4,.5 -3,3 1,4 -4,-2 -4,2 1,-4 -3,-3 4,-.5z"/>
      </g>
    </svg>
    <div class="abs serif" style="left:16px;top:59px;font-size:16px">1 = Needs Improvement</div>
    <div class="abs serif" style="left:288px;top:59px;font-size:16px">3 = Meets Expectations</div>
    <div class="abs serif" style="left:593px;top:59px;font-size:16px">5 = Excellent</div>
  </section>

  <!-- call handling -->
  <section class="band band--grey" style="top:347px;height:210px">
    <svg class="abs" style="left:16px;top:8px" width="34" height="34" viewBox="0 0 34 34" aria-hidden="true">
      <path d="M8,4 L13,10 L10,14 C12,19 15,22 20,24 L24,21 L30,26 L26,31 C14,30 4,20 3,8 Z" fill="none" stroke="var(--magenta)" stroke-width="2.2" stroke-linejoin="round"/>
      <path d="M30,3 L20,13 M20,6 V13 H27" fill="none" stroke="var(--magenta)" stroke-width="2.2"/>
    </svg>
    <div class="abs heading section-title" style="left:64px;top:6px">Call Handling &amp; First Call Intake</div>
    <div class="abs serif" style="left:64px;top:49px;font-size:16px;color:var(--indigo)">Task</div>
    <div class="abs serif" style="left:423px;top:49px;font-size:16px;color:var(--indigo)">Self-Rating (1-5)</div>
    <div class="abs serif" style="left:575px;top:49px;font-size:16px;color:var(--indigo)">Notes / Issues</div>
    <div class="abs task" style="top:81px">Answered 90%+ calls within 3 rings</div>
    <div class="abs task" style="top:114px">Maintained empathy and professionalism</div>
    <div class="abs task" style="top:146px">Accurately completed all First Call fields</div>
    <div class="abs task" style="top:179px">Worked within Receptionist role</div>
    <div class="rule" style="left:416px;top:97px;width:135px"></div><div class="rule" style="left:559px;top:97px;width:136px"></div>
    <div class="rule" style="left:416px;top:130px;width:135px"></div><div class="rule" style="left:559px;top:130px;width:136px"></div>
    <div class="rule" style="left:416px;top:162px;width:135px"></div><div class="rule" style="left:559px;top:162px;width:136px"></div>
    <div class="rule" style="left:416px;top:195px;width:135px"></div><div class="rule" style="left:559px;top:195px;width:136px"></div>
  </section>

  <!-- daily status -->
  <section class="band" style="top:557px;height:129px;background:var(--white)">
    <svg class="abs" style="left:18px;top:12px" width="32" height="32" viewBox="0 0 32 32" aria-hidden="true">
      <g fill="var(--magenta)"><rect x="2" y="20" width="4" height="10"/><rect x="9" y="16" width="4" height="14"/><rect x="16" y="12" width="4" height="18"/><rect x="23" y="8" width="4" height="22"/></g>
      <path d="M2,14 L14,6 L20,8 L29,2 M24,2 H29 V7" fill="none" stroke="var(--magenta)" stroke-width="2"/>
    </svg>
    <div class="abs heading section-title" style="left:63px;top:17px">Daily Status Summary <small>(Circle One)</small></div>
    <div class="abs radio" style="left:62px;top:63px"></div>
    <div class="abs option" style="left:88px;top:60px">Excellent</div>
    <div class="abs option-desc" style="left:88px;top:81px">All key duties completed,<br>proactive, calm under pressure</div>
    <div class="abs radio" style="left:316px;top:63px"></div>
    <div class="abs option" style="left:341px;top:60px">Satisfactory</div>
    <div class="abs option-desc" style="left:341px;top:81px">Most duties completed,<br>minor follow-up needed</div>
    <div class="abs radio" style="left:527px;top:63px"></div>
    <div class="abs option" style="left:552px;top:60px">Needs Support</div>
    <div class="abs option-desc" style="left:552px;top:81px">Missed urgent duties,<br>accuracy or stress issues</div>
  </section>

  <!-- daily reflection -->
  <section class="band band--grey" style="top:686px;height:114px">
    <svg class="abs" style="left:12px;top:14px" width="42" height="28" viewBox="0 0 42 28" aria-hidden="true">
      <g fill="none" stroke="var(--magenta)" stroke-width="2">
        <path d="M3,26 A18,18 0 0 1 39,26"/><path d="M10,26 A11,11 0 0 1 32,26"/>
        <path d="M8,10 L11,13 M21,4 V8 M34,10 L31,13"/><circle cx="21" cy="21" r="3"/><path d="M16,26 A5,5 0 0 1 26,26"/>
      </g>
    </svg>
    <div class="abs heading section-title" style="left:63px;top:16px">Daily Reflection</div>
    <div class="abs question" style="left:62px;top:49px"><b>?</b>What went well today?</div>
    <div class="abs question" style="left:251px;top:49px"><b>?</b>Any issues or barriers to note?</div>
    <div class="abs question" style="left:490px;top:49px"><b>?</b>Support needed from supervisor?</div>
    <div class="rule" style="left:78px;top:80px;width:134px"></div><div class="rule" style="left:78px;top:102px;width:134px"></div>
    <div class="rule" style="left:268px;top:80px;width:181px"></div><div class="rule" style="left:268px;top:102px;width:181px"></div>
    <div class="rule" style="left:502px;top:80px;width:201px"></div><div class="rule" style="left:502px;top:102px;width:201px"></div>
  </section>

  <!-- stars & flags -->
  <section class="band" style="top:800px;height:143px;background:var(--white)">
    <svg class="abs" style="left:12px;top:20px" width="46" height="22" viewBox="0 0 46 22" aria-hidden="true">
      <path d="M10,1 l2.8,6 6.4,.8 -4.7,4.4 1.2,6.3 -5.7,-3.2 -5.7,3.2 1.2,-6.3 -4.7,-4.4 6.4,-.8z" fill="none" stroke="var(--star)" stroke-width="1.8"/>
      <path d="M27,21 V2 H40 L37,7 L40,12 H27" fill="none" stroke="var(--indigo)" stroke-width="1.8"/>
    </svg>
    <div class="abs heading section-title section-title--indigo" style="left:63px;top:15px">Stars &amp; Flags <small style="color:var(--magenta)">(Supervisor Use Only)</small></div>
    <svg class="abs" style="left:28px;top:121px" width="0" height="0" aria-hidden="true"></svg>
    <svg class="abs" style="left:28px;top:60px" width="20" height="20" viewBox="0 0 20 20" aria-hidden="true"><path d="M10,1 l2.7,5.7 6.2,.8 -4.5,4.3 1.1,6.1 -5.5,-3 -5.5,3 1.1,-6.1 -4.5,-4.3 6.2,-.8z" fill="none" stroke="var(--star)" stroke-width="1.6"/></svg>
    <div class="abs sub" style="left:54px;top:64px">Stars <span>(Excellence or above-and-beyond moments)</span></div>
    <svg class="abs" style="left:406px;top:62px" width="18" height="20" viewBox="0 0 18 20" aria-hidden="true"><path d="M2,19 V2 H15 L12,6 L15,10 H2" fill="none" stroke="var(--indigo)" stroke-width="1.5"/></svg>
    <div class="abs sub" style="left:428px;top:64px">Flags <span>(Concerns needing follow-up/coaching)</span></div>
    <div class="rule" style="left:26px;top:98px;width:326px"></div><div class="rule" style="left:26px;top:120px;width:326px"></div>
    <div class="rule" style="left:406px;top:98px;width:306px"></div><div class="rule" style="left:406px;top:120px;width:306px"></div>
  </section>

  <!-- footer -->
  <footer class="band band--footer" style="top:943px;height:106px">
    <svg class="abs" style="left:12px;top:12px" width="52" height="44" viewBox="0 0 52 44" aria-hidden="true">
      <g fill="var(--star)">
        <path d="M26,0 l2,4 4.4,.6 -3.2,3 .8,4.4 -4,-2.1 -4,2.1 .8,-4.4 -3.2,-3 4.4,-.6z"/>
        <path d="M12,6 l1.6,3.2 3.5,.5 -2.5,2.4 .6,3.5 -3.2,-1.7 -3.2,1.7 .6,-3.5 -2.5,-2.4 3.5,-.5z"/>
        <path d="M40,6 l1.6,3.2 3.5,.5 -2.5,2.4 .6,3.5 -3.2,-1.7 -3.2,1.7 .6,-3.5 -2.5,-2.4 3.5,-.5z"/>
        <path d="M4,18 l1.3,2.6 2.8,.4 -2,2 .5,2.8 -2.6,-1.4 -2.6,1.4 .5,-2.8 -2,-2 2.8,-.4z"/>
        <path d="M48,18 l1.3,2.6 2.8,.4 -2,2 .5,2.8 -2.6,-1.4 -2.6,1.4 .5,-2.8 -2,-2 2.8,-.4z"/>
      </g>
      <rect x="14" y="28" width="6" height="14" fill="#6fa8dc"/>
      <path d="M21,29 H27 L28,20 C28,17 32,17 32,21 V27 H38 C41,27 41,31 38,31 C41,32 40,35 37,35 C39,36 38,39 35,39 H21 Z" fill="#f4c7a1"/>
    </svg>
    <div class="abs footer-label" style="left:77px;top:19px">Manager's Overall Rating</div>
    <div class="abs serif" style="left:77px;top:42px;font-size:9px">Performance On A 1-5 Scale</div>
    <div class="rule" style="left:77px;top:88px;width:202px;border-color:#8b86c4"></div>
    <div class="abs footer-label" style="left:406px;top:17px">Receptionist Signature</div>
    <div class="abs footer-label" style="left:406px;top:43px">Supervisor Signature</div>
    <div class="abs footer-label" style="left:406px;top:72px">Date</div>
    <div class="rule" style="left:594px;top:34px;width:130px;border-color:#8b86c4"></div>
    <div class="rule" style="left:594px;top:61px;width:130px;border-color:#8b86c4"></div>
    <div class="rule" style="left:594px;top:90px;width:130px;border-color:#8b86c4"></div>
  </footer>

</main>
</div>
</body>
</html>
```